Bramwell Garden Maintenance - Needs a business card! Easy JOB!

I need a business card for a new company called Bramwell Garden Maintenance. I will be offering the below services.

I am relatively open for ideas, so please be at your creative best.

I think I will list all the services offered on the rear of the card.

- Gardening
- Lawn Care
- Hedge Trimming
- Rubbish Removal
- Weeding/Spraying
- Landscaping
- Gutter Cleaning
- Solar Panel Cleaning
- Irrigation
- Pruning
- On-Site Mulching
- Ask for other services

I am still a little undecided on the colours. I prefer the logos with the Blue text, but I am open for ideas ( the logo/texts colours are not final).

Please use the catch phrase "What can Bramwell do for you?"

Here are the required details.

Bramwell Garden Maintenance

Neil Harcourt (owner)
Ph: 1300 XXX XXX
Mob: 0427 XXX XXX

neil@bramwellgarden.com.au
www.bramwellgarden.com.au
facebook.com/BramwellGarden
twitter.com/BramwellGarden
ABN: XXX XXX XXX ( this can be in smaller text somewhere, this is the least important )

Thankyou in advance! And good luck.

regards,
Neil
Updates

Hi everyone, please make sure you include the phrase "What can Bramwell do for you?" on the designs.

thanks,
Neil

Definitely liking the focus on a majority of the design on the blue colour from the logo. Also a splash of green in the plant.

Please make sure you list the services provided on the rear of the card. thanks.

With the service listing, please make "ask for other services" stand out, either a different colour or position or size... as long as it is more noticeable than the other services listed. Thanks.

Industry/Entity Type

Business

Requirements
Must have
• - use the font supplied (Brandon Family Font)
- use of the catch phrase "What can Bramwell do for you?"
- Double sided design
- Facebook and Twitter logos/links
- Please use symbol/picture for "phone" "mobile" "email" instead of using the words.
- List the services provided on the rear of the card

```html
<!DOCTYPE html>
<html lang="en">
<head>
<meta charset="utf-8">
<title>Bramwell Garden Maintenance – Business Card</title>
<link href="https://fonts.googleapis.com/css2?family=Montserrat:wght@300;400;600;700;900&display=swap" rel="stylesheet">
<style>
  :root {
    --stage: #e9ecef;
    --blue-deep: #1a6fb5;
    --blue-mid: #2389cc;
    --blue-light: #3aa5de;
    --brand-blue: #1c5aa0;
    --ink-line: #1d4d78;
    --icon: #1e4f7a;
    --white: #ffffff;
    --paper-grey: #d9dcdf;
    --abn: #3a4550;
    --accent-yellow: #f6e51b;
  }
  * { box-sizing: border-box; margin: 0; padding: 0; }
  html, body { width: 1200px; height: 900px; overflow: hidden; }
  body {
    background: var(--stage);
    font-family: "Montserrat", sans-serif;
    position: relative;
  }
  .card {
    position: absolute;
    border-radius: 8px;
    overflow: hidden;
    box-shadow: 0 10px 28px rgba(0,0,0,.18);
    background: radial-gradient(ellipse at 65% 40%, var(--blue-light) 0%, var(--blue-mid) 45%, var(--blue-deep) 100%);
  }

  /* ---------- Front ---------- */
  .card-front { left: 60px; top: 267px; width: 640px; height: 366px; }
  .card-front .shapes { position: absolute; inset: 0; }
  .brand-name {
    position: absolute;
    left: 14px; top: 178px;
    width: 170px;
    transform: rotate(-90deg);
    transform-origin: left top;
    color: var(--brand-blue);
    font-weight: 700;
    font-size: 22px;
    line-height: 22px;
    text-transform: uppercase;
    letter-spacing: .5px;
  }
  .brand-mark {
    position: absolute;
    left: 22px; top: 222px;
    width: 64px; height: 64px;
    border-radius: 50%;
    background: var(--brand-blue);
  }
  .person {
    position: absolute;
    left: 230px; top: 38px; width: 370px;
    text-align: center;
    color: var(--white);
  }
  .person-name { font-weight: 700; font-size: 31px; line-height: 36px; }
  .person-role { font-weight: 600; font-size: 11px; color: #eaf4fb; margin-top: -2px; }
  .contacts {
    position: absolute; left: 232px; top: 116px;
    list-style: none;
  }
  .contacts li {
    display: flex; align-items: center;
    height: 37px;
    color: var(--white);
    font-weight: 400;
    font-size: 19px;
  }
  .contacts li.email { font-size: 17px; }
  .contacts svg { width: 26px; height: 24px; margin-right: 18px; flex: none; }
  .web {
    position: absolute; left: 232px; top: 238px;
    display: flex; align-items: center;
    color: var(--white); font-size: 17px;
  }
  .web svg { width: 24px; height: 24px; margin-right: 20px; }
  .social {
    position: absolute; left: 394px; top: 276px;
    display: flex; gap: 10px;
  }
  .social span {
    width: 32px; height: 32px; border-radius: 5px;
    background: #4a6fa8;
    box-shadow: 0 1px 3px rgba(0,0,0,.25);
  }
  .social span + span { background: #6cc4e6; }
  .abn {
    position: absolute; left: 306px; top: 335px;
    color: var(--abn); font-size: 11px; letter-spacing: .3px;
  }

  /* ---------- Back ---------- */
  .card-back {
    left: 774px; top: 130px; width: 366px; height: 640px;
    padding: 40px 22px 0 30px;
    color: var(--white);
  }
  .headline {
    font-weight: 900;
    text-transform: uppercase;
    text-align: right;
    font-size: 46px;
    line-height: 50px;
    letter-spacing: -.5px;
  }
  .headline .brand-word { display: block; color: var(--accent-yellow); font-size: 50px; line-height: 56px; }
  .headline .tail { display: block; font-size: 37px; line-height: 44px; }
  .services {
    list-style: none;
    margin-top: 24px;
    padding-left: 14px;
    font-weight: 600;
    font-size: 19px;
    line-height: 30px;
    text-transform: uppercase;
  }
  .services li::before { content: "- "; }
  .ask-more {
    position: absolute; left: 30px; bottom: 30px;
    color: var(--accent-yellow);
    font-weight: 900;
    font-size: 19px;
    text-transform: uppercase;
  }
</style>
</head>
<body>

<section class="card card-front" aria-label="Business card front">
  <svg class="shapes" viewBox="0 0 640 366" aria-hidden="true">
    <path d="M0 0 H112 C104 130 122 262 196 366 H0 Z" fill="var(--white)"/>
    <line x1="0" y1="196" x2="116" y2="196" stroke="var(--paper-grey)" stroke-width="2"/>
    <path d="M190 366 C330 318 480 298 640 300 V366 Z" fill="var(--white)"/>
    <line x1="226" y1="28" x2="604" y2="28" stroke="var(--ink-line)" stroke-width="1.5"/>
    <line x1="226" y1="100" x2="604" y2="100" stroke="var(--ink-line)" stroke-width="1.5"/>
    <line x1="226" y1="228" x2="604" y2="228" stroke="var(--ink-line)" stroke-width="1.5"/>
  </svg>

  <div class="brand-name">Bramwell<br>Garden<br>Maintenance</div>
  <div class="brand-mark" aria-hidden="true"></div>

  <div class="person">
    <div class="person-name">Neil Harcourt</div>
    <div class="person-role">owner</div>
  </div>

  <ul class="contacts">
    <li>
      <svg viewBox="0 0 26 24" aria-label="Phone"><path d="M3 8 C3 4 23 4 23 8 L21 10 L17 9 L17 7 C14 6 12 6 9 7 L9 9 L5 10 Z" fill="var(--icon)"/><rect x="6" y="12" width="14" height="9" rx="2" fill="var(--icon)"/></svg>
      1300 XXX XXX
    </li>
    <li>
      <svg viewBox="0 0 26 24" aria-label="Mobile"><rect x="8" y="1" width="11" height="22" rx="2" fill="var(--icon)"/><rect x="10" y="4" width="7" height="7" fill="#8fc6ea"/></svg>
      0427 XXX XXX
    </li>
    <li class="email">
      <svg viewBox="0 0 26 24" aria-label="Email"><rect x="2" y="5" width="22" height="15" fill="var(--icon)"/><path d="M2 5 L13 14 L24 5" stroke="#8fc6ea" stroke-width="1.5" fill="none"/></svg>
      neil@bramwellgarden.com.au
    </li>
  </ul>

  <div class="web">
    <svg viewBox="0 0 24 24" aria-label="Website"><circle cx="12" cy="12" r="10" fill="none" stroke="var(--icon)" stroke-width="2"/><ellipse cx="12" cy="12" rx="4.5" ry="10" fill="none" stroke="var(--icon)" stroke-width="1.5"/><line x1="2" y1="12" x2="22" y2="12" stroke="var(--icon)" stroke-width="1.5"/></svg>
    www.bramwellgarden.com.au
  </div>

  <div class="social" aria-hidden="true"><span></span><span></span></div>
  <div class="abn">ABN: XXX XXX XXX</div>
</section>

<section class="card card-back" aria-label="Business card back">
  <h1 class="headline">What can <span class="brand-word">Bramwell</span><span class="tail">do for you?</span></h1>
  <ul class="services">
    <li>Gardening</li>
    <li>Lawn Care</li>
    <li>Hedge Trimming</li>
    <li>Rubbish Removal</li>
    <li>Weeding/Spraying</li>
    <li>Landscaping</li>
    <li>Gutter Cleaning</li>
    <li>Solar Panel Cleaning</li>
    <li>Irrigation</li>
    <li>Pruning</li>
    <li>On-Site Mulching</li>
  </ul>
  <p class="ask-more">Ask for other services</p>
</section>

</body>
</html>
```